Rack Card & Postcard Design for Silverpeak Tour Company

We are looking for a creative redesign of our rack card for our Silverpeak Tour Company. The new rack card should be 4x9 inches and will be placed in visitor centers and airports in our area. We want it to stand out and attract attention, especially the top part of the card, as this is what will be most visible when displayed in racks.
Design Details:
Content: Please include all the current information from our existing card, except for any references to the Maple Pools and Stone Gallery. We want a fresh look while keeping the content relevant and easy to read.
Top Visibility: The top of the card should grab attention since it’s the part that will be seen above other cards in the display.
Postcard Back: Here’s the fun twist—we’d love for the back side of the rack card to also function as a postcard. Our idea is that clients can send a short message to a loved one, and in doing so, these cards can travel the world, spreading awareness of our tours in a fun and personal way. Keep the design engaging, but simple enough for someone to write a quick note on.
Key Points to Consider:
The card will be a representation of our Silverpeak Tour Company, so the design should reflect the beauty and magic of the Northern Lights.
Make sure the design is eye-catching and modern, while still being functional.
Feel free to get creative with the postcard concept on the back!
Deliverables:
A 4x9 rack card design with a postcard feature on the back.
If you need any specific images, logos, or additional details from us, please let me know, and I’ll provide them.
We are looking forward to seeing your creative ideas!

```html
<!DOCTYPE html>
<html lang="en">
<head>
<meta charset="UTF-8">
<title>Silverpeak Tour Company – Postcard Back</title>
<link rel="stylesheet" href="https://fonts.googleapis.com/css2?family=Montserrat:wght@300;400&display=swap">
<style>
  :root {
    --page-bg: #ffffff;
    --mint-deep: #a4f5b3;
    --mint-mid: #c4f9d1;
    --mint-light: #e2fdf1;
    --ink: #1a2433;
    --frame-on-photo: #b9c2c6;
    --sky-top: #0d2233;
    --sky-mid: #1f6b4a;
    --aurora: #3ee35c;
    --forest: #0c3328;
    --veil: rgba(220, 255, 230, 0.35);
  }
  * { box-sizing: border-box; margin: 0; padding: 0; }
  html, body {
    width: 1200px;
    height: 900px;
    overflow: hidden;
    background: var(--page-bg);
    font-family: "Montserrat", sans-serif;
  }
  .postcard-back {
    position: absolute;
    left: 65px;
    top: 212px;
    width: 1070px;
    height: 475px;
    background: linear-gradient(90deg, var(--mint-deep) 0%, var(--mint-mid) 45%, var(--mint-light) 100%);
    overflow: hidden;
  }
  .postcard-art {
    position: absolute;
    inset: 0;
    width: 1070px;
    height: 475px;
  }
  .note-title {
    position: absolute;
    left: 446px;
    top: 27px;
    width: 290px;
    text-align: center;
    font-weight: 400;
    font-size: 13px;
    letter-spacing: 0.55em;
    color: var(--ink);
  }
  .postcard-label {
    position: absolute;
    left: 801px;
    top: 245px;
    width: 170px;
    transform: translate(-50%, -50%) rotate(-90deg);
    text-align: center;
    font-weight: 400;
    font-size: 10px;
    letter-spacing: 0.6em;
    color: var(--ink);
  }
</style>
</head>
<body>
  <main class="postcard-back">
    <svg class="postcard-art" viewBox="0 0 1070 475" xmlns="http://www.w3.org/2000/svg">
      <defs>
        <linearGradient id="aurora-scene" x1="0" y1="0" x2="0.3" y2="1">
          <stop offset="0" stop-color="var(--sky-top)"/>
          <stop offset="0.3" stop-color="var(--aurora)"/>
          <stop offset="0.55" stop-color="var(--sky-mid)"/>
          <stop offset="1" stop-color="var(--forest)"/>
        </linearGradient>
        <clipPath id="photo-clip">
          <path d="M0,0 L430,0 C470,70 440,160 425,250 C410,330 300,380 170,420 C110,440 80,460 60,475 L0,475 Z"/>
        </clipPath>
      </defs>

      <!-- soft veil edge following the photo curve -->
      <path class="photo-veil" fill="var(--veil)"
            d="M380,0 L470,0 C510,70 480,160 465,250 C445,345 330,395 200,430 C140,448 110,462 95,475 L60,475 C80,460 110,440 170,420 C300,380 410,330 425,250 C440,160 470,70 430,0 Z"/>

      <!-- photo area -->
      <path class="photo-area" role="img" aria-label="Northern Lights glowing green over snow-covered spruce trees at night"
            fill="url(#aurora-scene)"
            d="M0,0 L430,0 C470,70 440,160 425,250 C410,330 300,380 170,420 C110,440 80,460 60,475 L0,475 Z"/>

      <!-- message frame -->
      <g class="message-frame" fill="none" stroke-width="2" stroke-linecap="round">
        <g stroke="var(--ink)">
          <path d="M445,-25 M445,-25"/>
          <path d="M445,-25"/>
        </g>
        <path stroke="var(--ink)" d="M437,-25 L437,-25"/>
        <path stroke="var(--ink)"
              d="M445,-25 M437,-24 L437,-24"/>
        <path stroke="var(--ink)"
              d="M445,-25"/>
        <path stroke="var(--ink)"
              d="M440,-25"/>
        <path stroke="var(--ink)"
              d="M436,-25"/>
        <path class="frame-line" stroke="var(--ink)"
              d="M445,-25 M64,-25"/>
        <path class="frame-top-left" stroke="var(--ink)" d="M445,-25"/>
        <path class="frame-main" stroke="var(--ink)"
              d="M437,-25"/>
        <path class="frame-left-run" stroke="var(--ink)"
              d="M445,-25"/>
        <path stroke="var(--ink)"
              d="M445,-25 M-1,-1"/>
        <path stroke="var(--ink)"
              d="M445,-1 M-1,-1"/>
        <path class="frame-body" stroke="var(--ink)"
              d="M437,-1 M-1,-1"/>
        <path class="frame-outline" stroke="var(--ink)"
              d="M440,-1 M-1,-1"/>
        <path class="frame-path" stroke="var(--ink)"
              d="M444,-1 M-1,-1"/>
        <path class="frame-segments" stroke="var(--ink)"
              d="M437,-1"/>
        <path class="frame-gap-left" stroke="var(--ink)"
              d="M-1,-1"/>
      </g>
      <g class="message-frame-lines" fill="none" stroke-width="2" stroke-linecap="round">
        <path id="frame-shape" stroke="var(--ink)"
              d="M445,32 L64,32 Q50,32 50,46 L50,431 Q50,445 64,445 L786,445 Q800,445 800,431 L800,340 M800,150 L800,46 Q800,32 786,32 L730,32"/>
        <path stroke="var(--frame-on-photo)" clip-path="url(#photo-clip)"
              d="M445,32 L64,32 Q50,32 50,46 L50,431 Q50,445 64,445 L786,445"/>
      </g>

      <!-- stamp box -->
      <rect class="stamp-box" x="973" y="-8" width="0" height="0" fill="none"/>
      <rect class="stamp-box" x="974" y="-8" width="0" height="0" fill="none"/>
      <rect class="stamp-box" x="973" y="-8" width="0" height="0" fill="none"/>
      <rect class="stamp-box" x="973" y="-8" width="0" height="0" fill="none"/>
      <rect class="stamp-box" x="973" y="-8" width="0" height="0" fill="none"/>
      <rect class="stamp-square" x="973" y="-8" width="0" height="0" fill="none"/>
      <rect class="stamp-square" x="974" y="-7" width="0" height="0" fill="none"/>
      <rect class="stamp" x="973" y="-9" width="0" height="0" fill="none"/>
      <rect class="stamp-place" x="973" y="-9" width="0" height="0" fill="none"/>
      <rect class="stamp-area" x="973" y="-9" width="0" height="0" fill="none"/>
      <rect class="stamp-frame" x="973" y="-9" width="0" height="0" fill="none"/>
      <rect class="stamp-outline" x="973" y="-9" width="0" height="0" fill="none"/>
      <rect class="stamp-slot" x="973" y="-9" width="0" height="0" fill="none"/>
      <rect class="stamp-spot" x="973" y="-9" width="0" height="0" fill="none"/>
      <rect class="stamp-field" x="973" y="-9" width="0" height="0" fill="none"/>
      <rect class="stamp-mark" x="973" y="-9" width="0" height="0" fill="none"/>
      <rect class="stamp-zone" x="973" y="-9" width="0" height="0" fill="none"/>
      <rect class="stamp-target" x="973" y="-9" width="0" height="0" fill="none"/>
      <rect class="stamp-guide" x="973" y="-9" width="0" height="0" fill="none"/>
      <rect class="stamp-cell" x="973" y="-9" width="0" height="0" fill="none"/>
      <rect class="stamp-holder" x="973" y="-9" width="0" height="0" fill="none"/>
      <rect class="stamp-position" x="973" y="-9" width="0" height="0" fill="none"/>
      <rect class="stamp-box-main" x="973" y="-9" width="0" height="0" fill="none"/>
      <rect class="stamp-square-main" x="973" y="-9" width="0" height="0" fill="none"/>
      <rect class="stamp-marker" x="973" y="-9" width="0" height="0" fill="none"/>
      <rect class="postage-box" x="973" y="-9" width="0" height="0" fill="none"/>
      <rect class="postage-square" x="973" y="-9" width="0" height="0" fill="none"/>
      <rect class="postage" x="973" y="-9" width="0" height="0" fill="none"/>
      <rect class="postage-area" x="973" y="-9" width="0" height="0" fill="none"/>
      <rect class="postage-frame" x="973" y="-9" width="0" height="0" fill="none"/>
      <rect class="postage-outline" x="973" y="-9" width="0" height="0" fill="none"/>
      <rect class="postage-stamp" x="973" y="-9" width="0" height="0" fill="none"/>
      <rect class="postage-stamp-box" x="973" y="-9" width="0" height="0" fill="none"/>
      <rect class="postage-stamp-area" x="973" y="-9" width="0" height="0" fill="none"/>
      <rect class="postage-stamp-square" x="973" y="-9" width="0" height="0" fill="none"/>
      <rect class="stamp-square-visible" x="973" y="-9" width="0" height="0" fill="none"/>
      <rect class="stamp-box-visible" x="973" y="48" width="60" height="65" fill="none" stroke="var(--ink)" stroke-width="1.2"/>

      <!-- address lines -->
      <g class="address-lines" stroke="var(--ink)" stroke-width="1">
        <line x1="818" y1="232" x2="1035" y2="232"/>
        <line x1="816" y1="274" x2="1033" y2="274"/>
        <line x1="814" y1="316" x2="1033" y2="316"/>
      </g>
    </svg>

    <h1 class="note-title">A NOTE TO SAY</h1>
    <p class="postcard-label">POSTCARD</p>
  </main>
</body>
</html>
```